Velarine Retractable Banner

I need a banner designed to advertise my skincare brand at a meeting. I want it to be eye-catching, yet elegant and modern and it should keep with my branding from my website (www.velarine-example.com). Please let me know if you need any addition files or photos.

I have included the specs for the size I plan to order.

```html
<!DOCTYPE html>
<html lang="en">
<head>
<meta charset="utf-8">
<title>Velarine Retractable Banner</title>
<link rel="stylesheet" href="https://fonts.googleapis.com/css2?family=Playfair+Display:wght@400;700&family=Poppins:wght@400;500&display=swap">
<style>
  :root {
    --backdrop: #fdd9ae;
    --paper: #f8f8f8;
    --bronze: #b5774a;
    --bronze-light: #d9a06e;
    --bronze-deep: #9c6238;
    --ink: #1c1c1c;
    --white: #ffffff;
    --photo-sky: #b9d6e4;
    --photo-teal: #6f97a5;
    --photo-warm: #d99a78;
  }
  * { margin: 0; padding: 0; box-sizing: border-box; }
  html, body { width: 1200px; height: 1000px; overflow: hidden; }
  body { background: var(--backdrop); position: relative; }

  .banner {
    position: absolute;
    left: 395px; top: 30px;
    width: 410px; height: 940px;
    background: var(--paper);
    overflow: hidden;
  }
  .banner-art { position: absolute; inset: 0; }

  .brand {
    position: absolute; left: 26px; top: 452px;
  }
  .brand-name {
    font-family: "Playfair Display", serif;
    font-weight: 700;
    font-size: 54px;
    line-height: 1;
    color: var(--bronze);
  }
  .brand-byline {
    font-family: "Poppins", sans-serif;
    font-size: 14px;
    color: var(--bronze);
    margin-top: 4px;
    padding-left: 36px;
  }

  .headline {
    position: absolute; left: 26px; top: 576px;
    font-family: "Playfair Display", serif;
    line-height: 1;
  }
  .headline-lead { display: block; font-size: 36px; font-weight: 400; color: var(--ink); letter-spacing: -0.5px; }
  .headline-main { display: block; font-size: 72px; font-weight: 700; color: var(--bronze); letter-spacing: -1px; margin-top: -2px; }

  .intro {
    position: absolute; left: 26px; top: 712px; width: 356px;
    font-family: "Poppins", sans-serif;
    font-size: 16px; line-height: 20px;
    color: var(--ink);
    text-align: justify;
  }

  .contact-bar {
    position: absolute; left: 0; bottom: 0;
    width: 100%; height: 46px;
    background: var(--bronze);
    display: flex; align-items: center; justify-content: space-between;
    padding: 0 8px;
    font-family: "Poppins", sans-serif;
    font-size: 9px; color: var(--white);
  }
  .contact-item { display: flex; align-items: center; gap: 4px; white-space: nowrap; }
  .contact-icon {
    width: 17px; height: 17px; border-radius: 50%;
    background: var(--white);
    display: flex; align-items: center; justify-content: center;
  }
</style>
</head>
<body>
  <main class="banner">
    <svg class="banner-art" viewBox="0 0 410 940" width="410" height="940">
      <defs>
        <linearGradient id="heroTone" x1="0" y1="0" x2="1" y2="1">
          <stop offset="0" stop-color="#cfe3ec"/>
          <stop offset="0.45" stop-color="var(--photo-warm)"/>
          <stop offset="1" stop-color="var(--photo-teal)"/>
        </linearGradient>
        <linearGradient id="productTone" x1="0" y1="0" x2="1" y2="1">
          <stop offset="0" stop-color="#3f5055"/>
          <stop offset="0.5" stop-color="#e9e4e0"/>
          <stop offset="1" stop-color="#e0a48a"/>
        </linearGradient>
        <linearGradient id="waveTone" x1="0" y1="0" x2="1" y2="0">
          <stop offset="0" stop-color="var(--bronze-deep)"/>
          <stop offset="0.6" stop-color="var(--bronze-light)"/>
          <stop offset="1" stop-color="var(--bronze)"/>
        </linearGradient>
      </defs>

      <path class="hero-photo" role="img" aria-label="Photo of a woman applying skincare while looking into a round mirror"
            fill="url(#heroTone)"
            d="M0,0 H410 V330 C300,318 200,330 120,350 C70,362 30,360 0,345 Z"/>

      <path class="wave-band" fill="url(#waveTone)"
            d="M0,345 C30,360 70,362 120,350 C200,330 300,318 410,330 V352 C300,342 210,362 130,395 C75,418 30,420 0,405 Z"/>
      <path class="wave-line" fill="none" stroke="var(--white)" stroke-width="2" opacity="0.7"
            d="M0,360 C40,375 80,374 130,360 C210,340 300,330 410,340"/>

      <path class="product-photo" role="img" aria-label="Photo of a woman holding a serum dropper bottle near her face"
            fill="url(#productTone)" stroke="var(--bronze)" stroke-width="2"
            d="M410,352 C360,342 300,348 258,364 C226,378 214,410 234,440 C254,470 262,502 272,540 C286,586 344,592 410,556 Z"/>
    </svg>

    <div class="brand">
      <div class="brand-name">Velarine</div>
      <div class="brand-byline">by dr. maren holloway</div>
    </div>

    <h1 class="headline">
      <span class="headline-lead">Love For</span>
      <span class="headline-main">Your Skin</span>
    </h1>

    <p class="intro">Velarine Skincare blends the power of science with the purity of nature to nourish, protect, and rejuvenate your skin. Our carefully crafted formulas are designed to enhance your natural beauty, giving you a healthy, radiant glow. Experience skincare that truly understands your skin because you deserve nothing less.</p>

    <footer class="contact-bar">
      <div class="contact-item">
        <span class="contact-icon">
          <svg width="10" height="8" viewBox="0 0 10 8"><rect x="0.5" y="0.5" width="9" height="7" fill="none" stroke="#b5774a"/><path d="M0.5,0.5 L5,4.5 L9.5,0.5" fill="none" stroke="#b5774a"/></svg>
        </span>
        info@velarine-example.com
      </div>
      <div class="contact-item">
        <span class="contact-icon">
          <svg width="10" height="10" viewBox="0 0 10 10"><path d="M2,1 L3.6,1 L4.3,3 L3.2,3.8 C3.8,5.2 4.8,6.2 6.2,6.8 L7,5.7 L9,6.4 L9,8 C9,8.6 8.5,9 8,9 C4.1,8.8 1.2,5.9 1,2 C1,1.5 1.4,1 2,1 Z" fill="none" stroke="#b5774a" stroke-width="0.9"/></svg>
        </span>
        5550142200
      </div>
      <div class="contact-item">
        <span class="contact-icon">
          <svg width="11" height="11" viewBox="0 0 11 11"><circle cx="5.5" cy="5.5" r="4.6" fill="none" stroke="#b5774a" stroke-width="0.9"/><ellipse cx="5.5" cy="5.5" rx="2" ry="4.6" fill="none" stroke="#b5774a" stroke-width="0.9"/><path d="M1,5.5 H10 M1.7,3.3 H9.3 M1.7,7.7 H9.3" stroke="#b5774a" stroke-width="0.9"/></svg>
        </span>
        www.velarine-example.com
      </div>
    </footer>
  </main>
</body>
</html>
```